Website Design for Door Distributor

Granite Hinge Works LLC distributes doors in the Southwestern region of the United States. We need a website design for our company launch.

We are looking for a website design that screams modern, and is easy to navigate. We want our customers to browse through our collections of doors with ease, while at the same time enjoy the feel of the website (more on how the website should feel below). Our logo is attached to help with the design process.

We expect this relationship to continue beyond the initial assignment, whether it includes additions or updates to the site. In that sense, we will only work with that designer who will specifically incorporate our ideas into the design, not a designer that submits a "one-size-fits-all" design. With that in mind, we are looking for a creative person who is willing to take some risks.

We are committed to minimizing the amount of revisions needed, so we encourage you to message us with any questions you may have throughout the process, especially in the earlier phases.

Thanks in advance for your time.

Target Market(s)

Home builders, commercial builders, developers, and upper-middle class/upper class customers. As you can see, our target market is of a more sophisticated type, so the design should be on the more serious side, and less playful. It should showcase a sense of class.

Industry/Entity Type

Requirements
Must have
• The home page should have a slideshow showcasing 4 to 5 different topics. See www.quillbranch.net for an example. The headings for each picture should be easily customizable (font, color, etc.). The user should also be able to click on the picture and be taken to the page that the pictures are linked to.

At the very top right of every page, there should be 2 header links: Download Brochure | Contact

There should be 5 static categories placed in one row at the top of each page. See www.morvik-tane.com for an example. Each of these categories should drop down when you rest your mouse over it and display a list of links. Again, this should be easily customizable and shown on every page of the site. This will serve as the navigation menu. Let us know if you need to know the exact amount of links for each category - hopefully we can customize it on our end fairly easily.

Categories: Home | Products | Gallery | Support | About Us

Home Page: Along with the above, the home page should include a welcome section that introduces the user to the site. There should also be sections for "Featured Product" and "Testimonial".

Featured product: this will include an image and short text.

Testimonial: this will include a quote, which should be easy for us to update weekly, and a link to "More Testimonials".
Should not have
• No clutter - instead, the design layout should be open and easy to navigate.

No cartoonish graphics - instead, the graphics should be sophisticated and modern.

No flash, no java.

```html
<!DOCTYPE html>
<html lang="en">
<head>
<meta charset="utf-8">
<title>Granite Hinge Works – Home</title>
<link href="https://fonts.googleapis.com/css2?family=Arimo:wght@400;700&family=Open+Sans:ital,wght@0,400;0,600;1,400&display=swap" rel="stylesheet">
<style>
:root{
  --brown:#7a5a3a;
  --brown-dark:#4a3020;
  --wood-1:#3a2416;
  --wood-2:#6b3f22;
  --ink:#222;
  --text:#777;
  --line:#ddd;
  --soft:#f2f2f2;
  --band:#333;
  --foot:#1f1f1f;
  --foot-top:#2a2a2a;
  --white:#fff;
}
*{box-sizing:border-box;margin:0;padding:0}
html,body{width:1200px;height:2388px;overflow:hidden}
body{position:relative;background:var(--white);font-family:"Open Sans",Arial,sans-serif;color:var(--text)}
.abs{position:absolute}
h1,h2,h3,h4,.head{font-family:"Arimo",Arial,sans-serif;color:var(--ink)}

/* top bar */
.topbar{left:0;top:0;width:1200px;height:22px;background:#f4f4f4;border-bottom:2px solid var(--brown);font-size:9px;color:#777}
.topbar .welcome{left:174px;top:5px}
.topbar .links{right:164px;top:5px;display:flex;gap:22px}
.topbar .links span{display:flex;align-items:center;gap:5px}

/* header */
.header{left:0;top:22px;width:1200px;height:86px;background:var(--white)}
.logo{left:174px;top:24px;width:126px;height:132px;background:var(--white);box-shadow:0 2px 6px rgba(0,0,0,.3);z-index:3;display:flex;flex-direction:column;align-items:center;justify-content:center;gap:8px}
.logo .mark{width:22px;height:22px;background:var(--brown)}
.logo .name{font-family:"Arimo",Arial,sans-serif;font-weight:700;color:var(--brown-dark);font-size:14px;text-align:center;line-height:1.15}
.nav{right:164px;top:62px;display:flex;gap:22px;font-family:"Arimo",Arial,sans-serif;font-size:13px;color:#333}
.nav span:first-child{color:var(--brown)}

/* hero */
.hero{left:0;top:108px;width:1200px;height:374px;background:linear-gradient(90deg,var(--wood-1),#4a2c18 40%,var(--wood-2) 70%,var(--wood-1))}
.hero-door{left:760px;top:0;width:264px;height:374px;background:linear-gradient(180deg,#8a4e24,#a8622d 50%,#7a421e)}
.hero .kicker{left:174px;top:88px;color:var(--white);font-size:27px;font-weight:700}
.hero .title{left:174px;top:124px;color:var(--white);font-size:40px;font-weight:700}
.hero .rule{left:174px;top:184px;width:282px;height:4px;background:var(--brown)}
.hero .sub{left:174px;top:200px;color:#eee;font-size:21px}
.hero .btn{left:174px;top:252px;width:78px;height:28px;background:#7d6448;color:var(--white);font-size:10px;display:flex;align-items:center;justify-content:center;border-radius:3px}
.dots{left:534px;top:348px;display:flex;gap:10px}
.dots i{width:12px;height:12px;background:var(--white);display:block}

.tagline{left:0;top:482px;width:1200px;height:54px;background:var(--band);color:var(--white);font-size:21px;display:flex;align-items:center;justify-content:center}

/* intro */
.intro-title{left:0;top:560px;width:1200px;text-align:center;font-size:25px;font-weight:700}
.intro-sub{left:0;top:596px;width:1200px;display:flex;justify-content:center;align-items:center;gap:10px;font-size:10px;color:#555}
.intro-sub .bar{width:320px;height:1px;background:var(--line)}
.intro-text{left:174px;top:648px;width:610px;font-size:11px;line-height:18px}
.intro-text p{margin-bottom:18px}
.intro-img{left:824px;top:656px;width:212px;height:78px;background:linear-gradient(180deg,#a77a48,#7b5530)}

.feature{top:860px;width:276px}
.feature .icon{left:0;top:0;width:30px;height:30px;border:1px solid #aaa;border-radius:50%}
.feature h3{position:absolute;left:46px;top:4px;font-size:13px}
.feature em{position:absolute;left:46px;top:22px;font-size:9px;color:#333}
.feature .body{position:absolute;left:0;top:54px;font-size:11px;line-height:17px;width:270px}
.feature .more{position:absolute;left:0;top:222px;font-size:11px;color:#3a7ac0}
.vdiv{top:860px;width:1px;height:240px;background:var(--line)}

/* featured products */
.products{left:0;top:1120px;width:1200px;height:390px;background:var(--soft)}
.products h2{position:absolute;left:0;top:26px;width:1200px;text-align:center;font-size:21px}
.card{top:76px;width:214px;height:238px;background:var(--white);box-shadow:0 1px 3px rgba(0,0,0,.15)}
.card .ph{position:absolute;left:0;top:2px;width:214px;height:128px;background:linear-gradient(180deg,#a77a48,#6e4a28)}
.card h4{position:absolute;left:0;top:144px;width:214px;text-align:center;font-size:13px}
.card p{position:absolute;left:14px;top:164px;width:186px;text-align:center;font-size:9px;line-height:13px;font-style:italic}
.card .rule{position:absolute;left:56px;top:198px;width:102px;height:3px;background:var(--brown)}
.card .more{position:absolute;left:0;top:210px;width:214px;text-align:center;font-size:10px;color:#3a7ac0}
.arrow{top:188px;width:30px;height:30px;border-radius:50%;background:#222}
.pdots{left:588px;top:360px;display:flex;gap:8px}
.pdots i{width:9px;height:9px;border-radius:50%;background:#bbb;display:block}
.pdots i:first-child{background:#777}

/* blog + testimonials */
.col-title{top:1534px;font-size:16px;font-weight:700}
.col-rule{top:1562px;width:420px;height:1px;background:var(--line)}
.list{top:1588px;width:420px;height:312px;background:#f4f4f4;border:1px solid #e4e4e4;overflow:hidden}
.scroll{position:absolute;right:2px;top:6px;width:6px;height:300px;background:#e2e2e2}
.scroll i{display:block;width:6px;height:120px;background:#aaa}
.post{position:absolute;left:20px;width:380px;height:140px}
.post .date{position:absolute;left:0;top:0;width:40px;height:48px;border:1px solid #ccc;background:var(--white);text-align:center;font-size:8px}
.post .date b{display:block;background:var(--brown);color:var(--white);font-weight:400;padding:2px 0}
.post h4{position:absolute;left:86px;top:4px;font-size:13px}
.post small{position:absolute;left:86px;top:22px;font-size:9px;font-style:italic;color:#333}
.post p{position:absolute;left:86px;top:42px;width:220px;font-size:11px;line-height:17px}
.post svg{position:absolute;right:14px;top:16px}
.testi{position:absolute;left:8px;width:400px;height:130px}
.testi .ava{position:absolute;left:0;top:8px;width:58px;height:54px;background:var(--white);border:1px solid #ddd}
.testi h4{position:absolute;left:76px;top:4px;font-size:13px}
.testi small{position:absolute;left:76px;top:22px;font-size:9px;font-style:italic;color:#333}
.testi p{position:absolute;left:76px;top:42px;width:260px;font-size:11px;line-height:17px}
.totop{left:1108px;top:1834px;width:36px;height:36px;border-radius:50%;background:#333}

/* contact band */
.contact{left:0;top:1930px;width:1200px;height:174px;background:var(--foot)}
.contact .strip{position:absolute;left:0;top:0;width:1200px;height:64px;background:var(--foot-top)}
.c-item{position:absolute;top:0;width:200px;text-align:center;color:var(--white)}
.c-item .val{position:absolute;top:18px;width:200px;font-family:"Arimo",Arial,sans-serif;font-weight:700;font-size:16px}
.c-item svg{position:absolute;left:90px;top:92px}
.c-item .lab{position:absolute;top:126px;width:200px;font-size:12px;font-weight:600}
.notch{position:absolute;left:92px;top:64px;width:0;height:0;border-left:8px solid transparent;border-right:8px solid transparent;border-top:8px solid var(--foot-top)}

/* footer */
.footer{left:0;top:2104px;width:1200px;height:212px;background:var(--foot);color:#aaa;font-size:11px}
.footer h4{color:var(--white);font-size:13px;font-weight:700;line-height:20px}
.newsletter{position:absolute;left:174px;top:30px;width:180px}
.newsletter p{margin-top:8px;line-height:15px}
.signup{margin-top:18px;display:flex;height:26px}
.signup .f{flex:1;background:var(--white);font-size:9px;color:#aaa;display:flex;align-items:center;padding-left:30px;position:relative}
.signup .f::before{content:"";position:absolute;left:0;top:0;width:22px;height:26px;background:var(--brown-dark)}
.signup .go{width:34px;background:var(--brown);color:var(--white);font-size:10px;display:flex;align-items:center;justify-content:center}
.fdiv{position:absolute;left:372px;top:30px;width:1px;height:150px;background:#444}
.links-col{position:absolute;left:396px;top:30px}
.links-col ul,.links-col2 ul{list-style:none;margin-top:8px}
.links-col li,.links-col2 li{line-height:25px;font-size:10px;display:flex;align-items:center;gap:8px}
.links-col2{position:absolute;left:616px;top:50px}
.tick{width:8px;height:8px}
.thumbs{position:absolute;left:838px;top:30px}
.grid{margin-top:10px;display:grid;grid-template-columns:repeat(4,36px);gap:12px}
.grid i{display:block;width:36px;height:36px;background:linear-gradient(135deg,#3f8a5a,#8ac0c8)}
.grid i:nth-child(odd){background:linear-gradient(135deg,#3a6f8a,#b083c0)}

.bottom{left:0;top:2316px;width:1200px;height:72px;background:var(--foot-top)}
.bottom .brand{position:absolute;left:174px;top:14px;font-family:"Arimo",Arial,sans-serif;font-weight:700;color:#6a5038;font-size:20px;letter-spacing:1px}
.bottom .copy{position:absolute;left:174px;top:40px;font-size:10px;color:#888}
.social{position:absolute;left:866px;top:16px;display:flex;gap:22px}
.social i{display:block;width:40px;height:40px;border-radius:50%;background:#4a4a4a}
</style>
</head>
<body>

<div class="abs topbar">
  <span class="abs welcome">Hello and welcome to Granite Hinge Works</span>
  <div class="abs links">
    <span><svg width="9" height="9" viewBox="0 0 10 10"><rect x="1" y="3" width="8" height="5" fill="#888"/><rect x="3" y="1" width="4" height="2" fill="#888"/></svg>Download Brochure</span>
    <span><svg width="9" height="9" viewBox="0 0 10 10"><rect x="1" y="2" width="8" height="6" fill="none" stroke="#888"/></svg>Contact Us</span>
  </div>
</div>

<div class="abs header"></div>
<div class="abs logo">
  <span class="mark"></span>
  <span class="name">GRANITE<br>HINGE WORKS</span>
</div>
<nav class="abs nav">
  <span>HOME</span><span>ABOUT</span><span>PRODUCTS ▾</span><span>GALLERY ▾</span><span>CONTACT</span>
</nav>

<section class="abs hero">
  <div class="abs hero-door" role="img" aria-label="Photo of a wooden entry door with a decorative glass panel"></div>
  <div class="abs kicker head">UNIQUE DESIGN</div>
  <div class="abs title head">Efficient Entry Doors</div>
  <div class="abs rule"></div>
  <div class="abs sub">We develop original products, innovative and quality high.</div>
  <div class="abs btn">View More</div>
  <div class="abs dots"><i></i><i></i><i></i><i></i></div>
</section>

<div class="abs tagline">“ Your, Tag line here add! ”</div>

<h2 class="abs intro-title">Granite Hinge Works</h2>
<div class="abs intro-sub"><span class="bar"></span>★ Short introduction ★<span class="bar"></span></div>
<div class="abs intro-text">
  <p>Welcome to Granite Hinge Works. We are a regional provider of exceptional window &amp; door solutions for the Pacific Northwest and Hawaiian islands. Drawing from a well of premier manufacturers, our goal is to assist you in selecting the best window and door solution for your unique custom home or commercial project.</p>
  <p>If you are seeking window replacement, we will enlist the help of a certified installer whom you can trust to provide you a timely and professional installation and warranty.</p>
  <p>For products and services not listed on our web page, give us a call at 505.010.7734 or email us.</p>
</div>
<div class="abs intro-img" role="img" aria-label="Photo of a furnished room with wooden furniture"></div>

<div class="abs feature" style="left:174px">
  <svg class="abs icon" viewBox="0 0 30 30"><circle cx="15" cy="15" r="14" fill="none" stroke="#aaa"/><path d="M15 8v14M11 12h8" stroke="#7a5a3a" stroke-width="2"/></svg>
  <h3>Products and Services</h3><em>Intelligent sense for every door</em>
  <div class="body">Refurbished electronics are tested for their functionalities and the defects. These refurbished electronics are returned by the customers without using it or resold by the manufacturer after repairing and ensuring the functions. So, there is no debate that refurbished electronics are as good as new one and available at cheap rate.</div>
  <span class="more">Read more...</span>
</div>
<div class="abs vdiv" style="left:452px"></div>
<div class="abs feature" style="left:466px">
  <svg class="abs icon" viewBox="0 0 30 30"><circle cx="15" cy="15" r="14" fill="none" stroke="#aaa"/><rect x="9" y="10" width="12" height="10" fill="none" stroke="#7a5a3a" stroke-width="2"/></svg>
  <h3>Our Gallery</h3><em>Intelligent sense for every door</em>
  <div class="body">There are lots of used construction and industrial machineries in the market which are used less by the users and can be modified and repaired. These machineries can be reused instead of buying new one. This will save our money and most importantly our planet. Let's Recycle.</div>
  <span class="more" style="top:188px">Read more...</span>
</div>
<div class="abs vdiv" style="left:746px"></div>
<div class="abs feature" style="left:760px">
  <svg class="abs icon" viewBox="0 0 30 30"><circle cx="15" cy="15" r="14" fill="none" stroke="#aaa"/><path d="M9 20h12M10 20v-6h10v6" fill="none" stroke="#7a5a3a" stroke-width="2"/></svg>
  <h3>Refurbished Furniture</h3><em>Intelligent sense for every door</em>
  <div class="body">There is a saying that "Old is Gold". People are buying new furniture for their homes and offices. But give it a thought that you can buy used/refurbished furniture to design your home and office. This will cost less and will give you the same look and feel, moreover you are helping the planet to get green. So why waste money when you can buy used and save money for future.</div>
  <span class="more">Read more...</span>
</div>

<section class="abs products">
  <h2>Featured Products</h2>
  <div class="abs card" style="left:30px"><div class="ph" role="img" aria-label="Product photo of a furnished room"></div><h4>European Window</h4><p>"Why we're so good at fitting windows and grow a plant..."</p><div class="rule"></div><div class="more">Read More...</div></div>
  <div class="abs card" style="left:332px"><div class="ph" role="img" aria-label="Product photo of a furnished room"></div><h4>European Window</h4><p>"Why we're so good at fitting windows and grow a plant..."</p><div class="rule"></div><div class="more">Read More...</div></div>
  <div class="abs card" style="left:634px"><div class="ph" role="img" aria-label="Product photo of a furnished room"></div><h4>European Window</h4><p>"Why we're so good at fitting windows and grow a plant..."</p><div class="rule"></div><div class="more">Read More...</div></div>
  <div class="abs card" style="left:936px"><div class="ph" role="img" aria-label="Product photo of a furnished room"></div><h4>European Window</h4><p>"Why we're so good at fitting windows and grow a plant..."</p><div class="rule"></div><div class="more">Read More...</div></div>
  <svg class="abs arrow" style="left:-14px" viewBox="0 0 30 30"><circle cx="15" cy="15" r="15" fill="#222"/><path d="M20 11l-4 4 4 4" stroke="#fff" stroke-width="2" fill="none"/></svg>
  <svg class="abs arrow" style="left:1184px" viewBox="0 0 30 30"><circle cx="15" cy="15" r="15" fill="#222"/><path d="M10 11l4 4-4 4" stroke="#fff" stroke-width="2" fill="none"/></svg>
  <div class="abs pdots"><i></i><i></i></div>
</section>

<h3 class="abs col-title" style="left:174px">Latest Blog Posts</h3>
<div class="abs col-rule" style="left:174px"></div>
<h3 class="abs col-title" style="left:616px">Recent Testimonials</h3>
<div class="abs col-rule" style="left:616px"></div>

<div class="abs list" style="left:174px">
  <div class="post" style="top:10px">
    <div class="date"><b>March</b>25, 2013</div>
    <h4>Refurbished Furniture</h4><small>at 10:38</small>
    <p>Pellentesque habitant morbi tristique senectus et netus et malesuada fames ac turpis egestas.</p>
    <svg width="14" height="20" viewBox="0 0 14 20"><path d="M3 3l7 7-7 7" stroke="#333" stroke-width="3" fill="none"/></svg>
  </div>
  <div class="post" style="top:160px">
    <div class="date"><b>March</b>25, 2013</div>
    <h4>Refurbished Furniture</h4><small>at 15:07</small>
    <p>Pellentesque habitant morbi tristique senectus et netus et malesuada fames ac turpis egestas.</p>
    <svg width="14" height="20" viewBox="0 0 14 20"><path d="M3 3l7 7-7 7" stroke="#333" stroke-width="3" fill="none"/></svg>
  </div>
  <div class="scroll"><i></i></div>
</div>

<div class="abs list" style="left:616px">
  <div class="testi" style="top:10px"><svg class="ava" viewBox="0 0 58 54"><rect width="58" height="54" fill="#fff"/><circle cx="24" cy="22" r="8" fill="none" stroke="#aaa"/><path d="M12 44c2-8 22-8 24 0" fill="none" stroke="#aaa"/><rect x="36" y="8" width="14" height="10" fill="none" stroke="#aaa"/></svg><h4>Dev Marlowe</h4><small>By Admin</small><p>Pellentesque habitant morbi tristique senectus et netus et malesuada fames ac turpis egestas.</p></div>
  <div class="testi" style="top:142px"><svg class="ava" viewBox="0 0 58 54"><rect width="58" height="54" fill="#fff"/><circle cx="24" cy="22" r="8" fill="none" stroke="#aaa"/><path d="M12 44c2-8 22-8 24 0" fill="none" stroke="#aaa"/><rect x="36" y="8" width="14" height="10" fill="none" stroke="#aaa"/></svg><h4>Dev Marlowe</h4><small>By Admin</small><p>Pellentesque habitant morbi tristique senectus et netus et malesuada fames ac turpis egestas.</p></div>
  <div class="testi" style="top:274px"><svg class="ava" viewBox="0 0 58 54"><rect width="58" height="54" fill="#fff"/><circle cx="24" cy="22" r="8" fill="none" stroke="#aaa"/><path d="M12 44c2-8 22-8 24 0" fill="none" stroke="#aaa"/><rect x="36" y="8" width="14" height="10" fill="none" stroke="#aaa"/></svg><h4>Dev Marlowe</h4><small>By Admin</small><p>Pellentesque habitant morbi tristique senectus et netus.</p></div>
  <div class="scroll"><i></i></div>
</div>

<svg class="abs totop" viewBox="0 0 36 36"><circle cx="18" cy="18" r="18" fill="#333"/><path d="M12 21l6-7 6 7z" fill="#fff"/></svg>

<section class="abs contact">
  <div class="strip"></div>
  <div class="c-item" style="left:174px"><div class="val">+1 505 010 2200</div><span class="notch"></span>
    <svg width="20" height="20" viewBox="0 0 20 20"><path d="M4 2l4 1 1 4-2 2c1 2 3 4 5 5l2-2 4 1 1 4-2 2C9 19 1 11 2 4z" fill="#fff"/></svg><div class="lab">Phone</div></div>
  <div class="c-item" style="left:396px"><div class="val">+1 505 010 4481</div><span class="notch"></span>
    <svg width="20" height="20" viewBox="0 0 20 20"><rect x="6" y="2" width="8" height="16" rx="1" fill="#fff"/><rect x="7.5" y="4" width="5" height="10" fill="#1f1f1f"/></svg><div class="lab">Cell</div></div>
  <div class="c-item" style="left:616px"><div class="val">hello@granitehinge.net</div><span class="notch"></span>
    <svg width="20" height="20" viewBox="0 0 20 20"><rect x="2" y="5" width="16" height="11" fill="#fff"/><path d="M2 5l8 6 8-6" stroke="#1f1f1f" fill="none"/></svg><div class="lab">Email</div></div>
  <div class="c-item" style="left:838px"><div class="val">24x7x365</div><span class="notch"></span>
    <svg width="20" height="20" viewBox="0 0 20 20"><path d="M3 10l5 5 9-10" stroke="#fff" stroke-width="3" fill="none"/></svg><div class="lab">Good Support</div></div>
</section>

<footer class="abs footer">
  <div class="newsletter">
    <h4>Granite Hinge Works<br>Newsletter</h4>
    <p>Enter your email and subscribe to our newsletter.</p>
    <div class="signup"><span class="f">Email Address</span><span class="go">Go</span></div>
  </div>
  <div class="fdiv"></div>
  <div class="links-col">
    <h4>Recent Links</h4>
    <ul>
      <li><svg class="tick" viewBox="0 0 8 8"><path d="M1 4l2 2 4-5" stroke="#7a5a3a" stroke-width="1.5" fill="none"/></svg>Home</li>
      <li><svg class="tick" viewBox="0 0 8 8"><path d="M1 4l2 2 4-5" stroke="#7a5a3a" stroke-width="1.5" fill="none"/></svg>About Us</li>
      <li><svg class="tick" viewBox="0 0 8 8"><path d="M1 4l2 2 4-5" stroke="#7a5a3a" stroke-width="1.5" fill="none"/></svg>Products</li>
      <li><svg class="tick" viewBox="0 0 8 8"><path d="M1 4l2 2 4-5" stroke="#7a5a3a" stroke-width="1.5" fill="none"/></svg>Gallery</li>
    </ul>
  </div>
  <div class="links-col2">
    <ul>
      <li><svg class="tick" viewBox="0 0 8 8"><path d="M1 4l2 2 4-5" stroke="#7a5a3a" stroke-width="1.5" fill="none"/></svg>Support</li>
      <li><svg class="tick" viewBox="0 0 8 8"><path d="M1 4l2 2 4-5" stroke="#7a5a3a" stroke-width="1.5" fill="none"/></svg>Blog</li>
      <li><svg class="tick" viewBox="0 0 8 8"><path d="M1 4l2 2 4-5" stroke="#7a5a3a" stroke-width="1.5" fill="none"/></svg>Contact</li>
    </ul>
  </div>
  <div class="thumbs">
    <h4>Recent Products</h4>
    <div class="grid" role="img" aria-label="Thumbnails of recent product photos">
      <i></i><i></i><i></i><i></i><i></i><i></i><i></i><i></i>
    </div>
  </div>
</footer>

<div class="abs bottom">
  <div class="brand">Granite Hinge Works</div>
  <div class="copy">© All Rights Reserved - 2014</div>
  <div class="social"><i></i><i></i><i></i></div>
</div>

</body>
</html>
```